High-End audio shop owner needs a business card

I need a personal Business Card for my Audio shop which exists since 1962. We offer high Quality brands, professional Attention and run our own repair-service-department. I look for a design which will be printed on high Quality paper and shall convey trust to the Client that we are very serious. Language is german.

```html
<!DOCTYPE html>
<html lang="de">
<head>
<meta charset="utf-8">
<title>Klangwerk Audio – Visitenkarte</title>
<link href="https://fonts.googleapis.com/css2?family=Montserrat:wght@400;600;800&display=swap" rel="stylesheet">
<style>
  :root {
    --page-bg: #5a5a5a;
    --card-bg: #2c2c2c;
    --card-edge: #242424;
    --text-light: #e6e6e6;
    --logo-silver: #d4d4d4;
    --accent: #e8671e;
    --deco-dark: #1c1c1c;
    --deco-mid: #3a3a3a;
  }
  * { margin: 0; padding: 0; box-sizing: border-box; }
  html, body {
    width: 1200px; height: 1021px; overflow: hidden;
    background: var(--page-bg);
    font-family: "Montserrat", sans-serif;
  }
  .stage {
    width: 1200px; height: 1021px;
    display: flex; flex-direction: column; align-items: center; justify-content: center;
    gap: 60px;
  }
  .card {
    width: 580px; height: 375px;
    background: var(--card-bg);
    border: 1px solid var(--card-edge);
    box-shadow: 0 14px 30px rgba(0,0,0,.35);
    position: relative;
  }
  .card-front {
    display: flex; align-items: center; justify-content: center;
  }
  .brand {
    display: flex; align-items: center; gap: 14px;
    color: var(--logo-silver);
    font-weight: 800; font-size: 40px; letter-spacing: 1px;
  }
  .brand-dot {
    width: 16px; height: 16px; border-radius: 50%;
    background: var(--logo-silver);
  }
  .card-back {
    display: flex; align-items: center; justify-content: space-between;
    padding: 0 0;
  }
  .speaker-deco {
    width: 120px; height: 230px;
  }
  .speaker-deco.left {
    background: linear-gradient(90deg, var(--deco-mid), var(--deco-dark));
  }
  .speaker-deco.right {
    background: linear-gradient(270deg, var(--deco-mid), var(--deco-dark));
  }
  .contact {
    flex: 1;
    text-align: center;
    color: var(--text-light);
    font-size: 17px; line-height: 1.3;
  }
  .contact-name {
    color: var(--accent); font-weight: 600; font-size: 22px;
  }
  .contact-role { font-size: 15px; margin-bottom: 14px; }
  .divider {
    position: relative; height: 26px; margin: 8px 24px;
    display: flex; align-items: center; justify-content: center; gap: 6px;
  }
  .divider::before {
    content: ""; position: absolute; left: 0; right: 0; top: 50%;
    border-top: 1.5px solid var(--accent);
  }
  .icon {
    position: relative; width: 24px; height: 24px; border-radius: 50%;
    background: var(--accent); display: flex; align-items: center; justify-content: center;
  }
  .icon svg { width: 14px; height: 14px; }
</style>
</head>
<body>
<main class="stage">
  <section class="card card-front">
    <div class="brand"><span class="brand-dot"></span><span class="brand-name">KLANGWERK AUDIO</span></div>
  </section>

  <section class="card card-back">
    <div class="speaker-deco left" role="img" aria-label="Dekorative Lautsprecher-Grafik, dunkel geprägt"></div>
    <div class="contact">
      <p class="contact-name">Lukas Brenner</p>
      <p class="contact-role">Owner</p>
      <p>Talackerweg 12</p>
      <p>CH-6004 Luzern</p>
      <div class="divider">
        <span class="icon"><svg viewBox="0 0 24 24" fill="none" stroke="#2c2c2c" stroke-width="2.4"><path d="M6 3h4l2 5-3 2a11 11 0 0 0 5 5l2-3 5 2v4a2 2 0 0 1-2 2A17 17 0 0 1 4 5a2 2 0 0 1 2-2z"/></svg></span>
        <span class="icon"><svg viewBox="0 0 24 24" fill="none" stroke="#2c2c2c" stroke-width="2.4"><rect x="3" y="6" width="18" height="12"/><path d="M3 6l9 7 9-7"/></svg></span>
        <span class="icon"><svg viewBox="0 0 24 24" fill="none" stroke="#2c2c2c" stroke-width="2"><circle cx="12" cy="12" r="9"/><path d="M3 12h18M12 3c3 3 3 15 0 18M12 3c-3 3-3 15 0 18"/></svg></span>
      </div>
      <p>041 555 01 72</p>
      <p>info@klangwerk-audio.ch</p>
      <p>www.klangwerk-audio.ch</p>
    </div>
    <div class="speaker-deco right" role="img" aria-label="Dekorative Lautsprecher-Grafik, dunkel geprägt"></div>
  </section>
</main>
</body>
</html>
```